Powerpoint Design and Build

We need to create PowerPoint for program called Kindled Horizons. Kindled Horizons is an online system that helps association volunteers track their volunteer hours and the impact that are having with engineering outreach initiatives.

We have an established logo for the brand, which you will find under Files.

The following colors are used in the brand:

Blue/green: PMS 3262 C

Purple: PMS 525 C

Lime: PMS 381 C

Grey: PMS Cool Grey 11

Headline and body fonts should be restricted to a common sans serif such as arial or helvetica

For reference, The tagline "Make Volunteering Count" is set in Gotham Book; match to this.

The identity needs to be locked up with the Alliance of Rural Planners logo in grey, which you'll find attached. See the file "Kindled_horizons_lock-up.psd" for reference, but please recreate as a vector element.

As an idea of Powerpoint created for a different Alliance of Rural Planners program, place see the Lantern Powerpoint. FOR Reference only

NOTE: please maximize the area for content and stick to a white background.

Final deliverables are:

Design for presentation title slide, section title slide and content slide, including styles for headlines, subheads, bullet points and straight copy. Also include slide numbers in footer.

To repeat, we expect separate art elements created in Illustrator, and a completed Powerpoint template with master slides.

Target Market(s)

Professional and Collegiate Women in Engineering

Industry/Entity Type

Engineering

Requirements
Must have
• Design for presentation title slide, section title slide and content slide, including styles for headlines, subheads, bullet points and straight copy. Also include slide numbers in footer.

```html
<!DOCTYPE html>
<html lang="en">
<head>
<meta charset="utf-8">
<title>Kindled Horizons – Section Title Slide</title>
<link rel="stylesheet" href="https://fonts.googleapis.com/css2?family=Montserrat:wght@300;400&display=swap">
<style>
  :root {
    --white: #ffffff;
    --lime: #d5df3a;
    --purple: #542c66;
    --teal: #10b2ae;
    --grey-text: #6d6e71;
    --band-dark: #b3b4b6;
    --band-light: #e4e4e5;
    --ink: #1a1a1a;
  }
  html, body {
    margin: 0;
    padding: 0;
    overflow: hidden;
    background: var(--white);
  }
  .slide {
    position: relative;
    width: 1200px;
    height: 848px;
    overflow: hidden;
    background: var(--white);
    font-family: "Montserrat", Arial, sans-serif;
  }
  .accent {
    position: absolute;
    top: 0;
    left: 0;
  }
  .lockup {
    position: absolute;
    top: 40px;
    left: 605px;
    height: 40px;
    display: flex;
    align-items: center;
  }
  .lockup__brand {
    display: flex;
    align-items: center;
    gap: 9px;
    font-size: 29px;
    font-weight: 300;
    color: var(--teal);
  }
  .lockup__brand-dot,
  .lockup__partner-dot {
    display: inline-block;
    border-radius: 50%;
  }
  .lockup__brand-dot {
    width: 30px;
    height: 30px;
    background: var(--teal);
  }
  .lockup__divider {
    width: 1px;
    height: 40px;
    background: #c8c8ca;
    margin: 0 20px 0 16px;
  }
  .lockup__partner {
    display: flex;
    align-items: center;
    gap: 8px;
    font-size: 17px;
    font-weight: 400;
    color: var(--grey-text);
    line-height: 1.05;
  }
  .lockup__partner-dot {
    width: 30px;
    height: 30px;
    background: var(--grey-text);
  }
  .section-title {
    position: absolute;
    top: 364px;
    left: 366px;
    margin: 0;
    font-size: 40px;
    font-weight: 300;
    letter-spacing: 0.8px;
    line-height: 1.2;
    color: var(--ink);
  }
  .footer-band {
    position: absolute;
    left: 0;
    top: 700px;
    width: 1200px;
    height: 148px;
    background: linear-gradient(90deg, var(--band-dark) 0%, #cfd0d1 45%, var(--band-light) 100%);
  }
  .footer-band__photo {
    position: absolute;
    right: 0;
    top: 0;
    width: 630px;
    height: 148px;
    background: linear-gradient(90deg, rgba(200,195,190,0) 0%, #b9aea6 25%, #c9bfb8 60%, #ddd6d0 100%);
  }
  .footer-band__tagline {
    position: absolute;
    left: 735px;
    top: 64px;
    margin: 0;
    font-size: 25px;
    font-weight: 400;
    color: var(--white);
  }
</style>
</head>
<body>
<div class="slide">
  <svg class="accent" width="1200" height="848" viewBox="0 0 1200 848" aria-hidden="true">
    <ellipse fill="var(--lime)" cx="80" cy="20" rx="220" ry="150"/>
    <ellipse fill="var(--purple)" cx="1210" cy="150" rx="170" ry="70"/>
  </svg>

  <div class="lockup">
    <div class="lockup__brand"><span class="lockup__brand-dot"></span>Kindled Horizons</div>
    <span class="lockup__divider"></span>
    <div class="lockup__partner"><span class="lockup__partner-dot"></span>Alliance of<br>Rural Planners</div>
  </div>

  <h1 class="section-title">SECTION TITLE SLIDE</h1>

  <div class="footer-band">
    <div class="footer-band__photo" role="img" aria-label="Photograph of four smiling women engineers"></div>
    <p class="footer-band__tagline">Make Volunteering Count</p>
  </div>

  <svg class="accent" width="1200" height="848" viewBox="0 0 1200 848" aria-hidden="true">
    <circle fill="var(--teal)" cx="150" cy="850" r="195"/>
  </svg>
</div>
</body>
</html>
```